landscaping core flute signs

I need core flutes created with business name and a few extra dot points for putting on fences for job sites 120cm x 120cm approx.
I want our old ones information with the new L logo and colour palette

```html
<!DOCTYPE html>
<html lang="en">
<head>
<meta charset="utf-8">
<title>Stonehaven Yards – Site Sign</title>
<link rel="stylesheet" href="https://fonts.googleapis.com/css2?family=Roboto:wght@400;500;700&display=swap">
<style>
  :root {
    --sign-black: #000000;
    --leaf-green: #5f8c58;
    --paper-white: #ffffff;
    --ink: #050505;
  }
  * { margin: 0; padding: 0; box-sizing: border-box; }
  html, body {
    width: 1200px;
    height: 1200px;
    overflow: hidden;
    background: var(--sign-black);
  }
  .sign {
    position: relative;
    width: 1200px;
    height: 1200px;
    background: var(--sign-black);
    font-family: "Roboto", Arial, sans-serif;
    color: var(--paper-white);
  }
  .brand-mark {
    position: absolute;
    left: 468px;
    top: 62px;
    width: 262px;
    height: 262px;
    border-radius: 50%;
    background: var(--leaf-green);
  }
  .brand-name {
    position: absolute;
    left: 0;
    top: 360px;
    width: 1200px;
    text-align: center;
    font-weight: 500;
    font-size: 76px;
    line-height: 1;
    color: var(--paper-white);
  }
  .tagline {
    position: absolute;
    left: 0;
    top: 464px;
    width: 1200px;
    text-align: center;
    font-weight: 500;
    font-size: 30px;
    line-height: 1;
    color: var(--paper-white);
  }
  .services {
    position: absolute;
    left: 307px;
    top: 584px;
    list-style: none;
  }
  .service {
    display: flex;
    align-items: center;
    height: 86px;
    font-weight: 500;
    font-size: 48px;
    color: var(--paper-white);
  }
  .service__dot {
    width: 60px;
    height: 60px;
    border-radius: 50%;
    background: var(--leaf-green);
    margin-right: 50px;
    flex: none;
  }
  .phone-band {
    position: absolute;
    left: 0;
    top: 878px;
    width: 1200px;
    height: 181px;
    background: var(--leaf-green);
    display: flex;
    align-items: center;
    justify-content: center;
  }
  .phone {
    font-weight: 700;
    font-size: 180px;
    line-height: 1;
    color: var(--ink);
    letter-spacing: 1px;
    margin-top: 4px;
  }
  .email-band {
    position: absolute;
    left: 0;
    top: 1059px;
    width: 1200px;
    height: 92px;
    display: flex;
    align-items: center;
    justify-content: center;
  }
  .email {
    font-weight: 400;
    font-size: 56px;
    color: var(--paper-white);
  }
  .footer-band {
    position: absolute;
    left: 0;
    top: 1151px;
    width: 1200px;
    height: 49px;
    background: var(--leaf-green);
  }
</style>
</head>
<body>
  <main class="sign">
    <div class="brand-mark" aria-hidden="true"></div>
    <h1 class="brand-name">Stonehaven Yards</h1>
    <p class="tagline">Structural Landscaping</p>

    <ul class="services">
      <li class="service"><span class="service__dot"></span>Paving &amp; Concreting</li>
      <li class="service"><span class="service__dot"></span>Fencing &amp; Retaining</li>
      <li class="service"><span class="service__dot"></span>Design &amp; Construct</li>
    </ul>

    <div class="phone-band">
      <p class="phone">0412 555 019</p>
    </div>
    <div class="email-band">
      <p class="email">sam@stonehavenyards.com</p>
    </div>
    <div class="footer-band"></div>
  </main>
</body>
</html>
```